Flyer for spiritual retreat (yoga, meditation, reiki, raw food)

I would like a flyer to promote my upcoming retreat and a matching Facebook banner.

The name of the retreat is "Wavecrest Of Calm" and the tagline is "retreat into you"

The activities in the retreat include daily meditation, ecstatic dance, spiritual development workshops on intuition, energy healing etc and a reiki session is included.

I would like a flyer designed to promote this, something that is editable as I will be running this multiple times and will need to adjust the flyer to add the dates etc each time.

edit: add that here will be fully catered raw food and juices, and that the retreat price includes all accomodation, meals and workshops.

Please contact me if you need further info. Please also visit my website www.marithovland.com and www.facebook.com/tolvanahaven to see my current events and promotions.

Thank you,

Marit

Reason: Hi all, thank you all for your submissions. Apologies as I am traveling and do not have much access to internet and will review your submissions and provide feedback as soon as possible. Kind regards, Marit.

Target Market(s)

People who like meditation, yoga, fans of rowan mabry and jasper vinek, those interested in personal and spiritual development.

Industry/Entity Type

Health And Wellness

Requirements
Must have
• Please put the included reiki session as as added bonus. Something like "BONUS 30 minute reiki healing session" in a little star/banner/something that stands out.
• Please emphasise the "light" part of Wavecrest as I am going for a play on words between in the light and enlightenment.
• Please include placeholder text for place, location, time
• Placeholder for price
• My name (see attached file - can change colour to suit) and website (www.marithovland.com)
Nice to have
• I prefer rounded designs, curves rather than block designs.
Should not have
• Tolvana Haven logo

```html
<!DOCTYPE html>
<html lang="en">
<head>
<meta charset="utf-8">
<title>Wavecrest Of Calm – Retreat Flyer</title>
<link href="https://fonts.googleapis.com/css2?family=Great+Vibes&family=Open+Sans:ital,wght@0,400;0,600;0,700;1,400&display=swap" rel="stylesheet">
<style>
  :root {
    --violet: #b84cf6;
    --periwinkle: #8a7cf6;
    --sky: #45bff2;
    --aqua: #3fe4f0;
    --lemon: #ece77a;
    --cream: #fbf2c8;
    --ink: #2b2b2b;
    --brown: #4e3a22;
    --rule: #8a6a45;
    --paper: #ffffff;
    --cloud-top: #f1ece2;
    --cloud-mid: #b9c8cf;
    --cloud-low: #5f7f8e;
  }
  * { margin: 0; padding: 0; box-sizing: border-box; }
  html, body { width: 960px; height: 1200px; overflow: hidden; background: var(--paper); }
  .flyer {
    position: relative; width: 960px; height: 1200px; overflow: hidden;
    background: var(--paper);
    font-family: "Open Sans", Arial, sans-serif; color: var(--ink);
  }
  .backdrop { position: absolute; inset: 0; }
  .motif { position: absolute; border-radius: 50%; }
  .motif--header-left {
    left: 45px; top: 540px; width: 170px; height: 170px;
    background: radial-gradient(circle, rgba(255,255,255,.35), rgba(255,255,255,.08) 70%, transparent 72%);
  }
  .motif--header-right {
    left: 690px; top: 560px; width: 330px; height: 330px;
    background: radial-gradient(circle, #8ff6fb 0%, var(--aqua) 55%, rgba(63,228,240,0) 72%);
  }
  .motif--corner {
    left: 600px; top: -60px; width: 380px; height: 300px;
    background: radial-gradient(ellipse, rgba(200,200,210,.35), rgba(220,220,225,.1) 65%, transparent 70%);
  }
  .motif--body {
    left: -60px; top: 640px; width: 520px; height: 420px;
    background: radial-gradient(ellipse, rgba(205,205,215,.32), rgba(220,220,228,.1) 65%, transparent 70%);
  }
  .sky-photo {
    position: absolute; left: 0; top: 930px; width: 960px; height: 270px;
    background: linear-gradient(180deg, rgba(241,236,226,0) 0%, var(--cloud-top) 10%, var(--cloud-mid) 55%, var(--cloud-low) 100%);
  }
  .sky-band {
    position: absolute; left: 0; top: 1092px; width: 960px; height: 56px;
    background: rgba(255,255,255,.55);
  }
  .host-name {
    position: absolute; left: 40px; top: 60px;
    font-family: "Great Vibes", cursive; font-size: 100px; line-height: 1;
    color: var(--paper); font-weight: 400;
  }
  .title {
    position: absolute; left: 40px; top: 262px; white-space: nowrap;
    font-weight: 600; color: var(--paper); line-height: 1;
    text-shadow: 0 6px 10px rgba(60,30,110,.35);
  }
  .title__main { font-size: 122px; color: var(--cream); letter-spacing: -2px; }
  .title__light { color: #fffbe6; }
  .title__rest { font-size: 44px; margin-left: 10px; }
  .tagline {
    position: absolute; left: 528px; top: 400px;
    font-size: 31px; font-style: italic; color: #1e1e3a;
  }
  .activities, .catering {
    position: absolute; left: 92px; width: 350px;
    font-size: 18.5px; font-style: italic; line-height: 1.42; color: #333;
  }
  .activities { top: 650px; }
  .catering { top: 866px; }
  .rating {
    position: absolute; left: 196px; top: 790px;
    font-size: 26px; letter-spacing: 8px; color: #6f6a4f;
  }
  .place { position: absolute; left: 474px; top: 663px; font-size: 24px; color: var(--ink); }
  .time { position: absolute; left: 778px; top: 807px; font-size: 24px; color: var(--ink); }
  .bonus {
    position: absolute; left: 460px; top: 773px; width: 212px; text-align: center; color: var(--brown);
  }
  .bonus__flourish { display: block; margin: 0 auto; }
  .bonus__label { font-size: 30px; font-weight: 600; letter-spacing: 9px; line-height: 1.2; margin-top: 8px; }
  .bonus__length { font-size: 33px; font-weight: 700; line-height: 1.1; }
  .bonus__detail { font-size: 17px; margin-bottom: 8px; }
  .price { position: absolute; left: 776px; top: 970px; font-size: 31px; font-weight: 700; color: var(--brown); }
  .website { position: absolute; left: 44px; top: 1036px; font-size: 30px; font-weight: 600; color: #1d1d1d; }
</style>
</head>
<body>
<main class="flyer">
  <svg class="backdrop" width="960" height="1200" viewBox="0 0 960 1200" aria-hidden="true">
    <defs>
      <linearGradient id="header-wash" x1="0" y1="0" x2="1" y2="0.55">
        <stop offset="0" stop-color="#b84cf6"/>
        <stop offset="0.5" stop-color="#8a7cf6"/>
        <stop offset="1" stop-color="#45bff2"/>
      </linearGradient>
    </defs>
    <path class="header-wash" fill="url(#header-wash)"
          d="M0 0 H960 V700 C880 690 760 640 640 560 C540 495 430 470 330 495 C200 530 90 600 0 650 Z"/>
    <path class="header-edge" fill="none" stroke="var(--lemon)" stroke-width="7"
          d="M0 650 C90 600 200 530 330 495 C430 470 540 495 640 560 C760 640 880 690 960 700"/>
    <path class="corner-wave" fill="var(--paper)"
          d="M760 0 C720 60 640 70 600 130 C560 190 580 215 650 212 C760 208 880 195 960 205 V0 Z"/>
    <path class="corner-edge" fill="none" stroke="var(--lemon)" stroke-width="6"
          d="M760 0 C720 60 640 70 600 130 C575 165 560 185 575 200"/>
  </svg>

  <div class="motif motif--corner" role="img" aria-label="Faint mandala pattern"></div>
  <div class="motif motif--header-left" role="img" aria-label="Faint white mandala"></div>
  <div class="motif motif--header-right" role="img" aria-label="Turquoise mandala ornament"></div>
  <div class="motif motif--body" role="img" aria-label="Faint grey mandala pattern"></div>

  <div class="sky-photo" role="img" aria-label="Photograph of sunlit clouds"></div>
  <div class="sky-band"></div>

  <svg class="backdrop" width="960" height="1200" viewBox="0 0 960 1200" aria-hidden="true">
    <line x1="434" y1="784" x2="434" y2="976" stroke="var(--rule)" stroke-width="2"/>
    <line x1="691" y1="760" x2="691" y2="920" stroke="var(--rule)" stroke-width="2"/>
    <path class="price-ribbon" fill="var(--cream)"
          d="M456 950 C560 900 690 970 800 940 C880 918 930 900 960 895 V1030 C880 1020 800 1040 700 1060 C600 1078 520 1062 456 1040 C520 1030 540 1000 456 950 Z"/>
  </svg>

  <div class="host-name">Marit Hovland</div>

  <h1 class="title"><span class="title__main">Wave<span class="title__light">crest</span></span><span class="title__rest">Of Calm</span></h1>
  <p class="tagline">retreat into you</p>

  <p class="activities">The activities in the retreat include daily meditation, ecstatic dance, spiritual development workshops on intuition, energy healing etc &amp; and a reiki session is included.</p>
  <p class="rating">★★★★</p>
  <p class="catering">here will be fully catered raw food and juices, and that the retreat price includes all accomodation, meals and workshops.</p>

  <p class="place">place, Location</p>

  <div class="bonus">
    <svg class="bonus__flourish" width="110" height="14" viewBox="0 0 110 14" aria-hidden="true">
      <path d="M0 7 H45 M65 7 H110" stroke="var(--rule)" stroke-width="1.5"/>
      <circle cx="55" cy="7" r="4" fill="none" stroke="var(--rule)" stroke-width="1.5"/>
    </svg>
    <p class="bonus__label">BONUS</p>
    <p class="bonus__length">30 minute</p>
    <p class="bonus__detail">reiki healing session</p>
    <svg class="bonus__flourish" width="110" height="14" viewBox="0 0 110 14" aria-hidden="true">
      <path d="M0 7 H45 M65 7 H110" stroke="var(--rule)" stroke-width="1.5"/>
      <circle cx="55" cy="7" r="4" fill="none" stroke="var(--rule)" stroke-width="1.5"/>
    </svg>
  </div>

  <p class="time">Time</p>
  <p class="price">Price</p>
  <p class="website">www.marithovland.com</p>
</main>
</body>
</html>
```